Company Mission & Values Poster

I'd like an A2 Portrait Poster displaying our company's Mission & Values.
See our website for our logo, fonts, mission & values.
https://talvendo.com.au/

Our Mission: Creating homes for abundant life
Values: Love, Thinking, Team, Zoe.

Some ideas to consider:
Mission as the Headline then
A logo for each of the 4 Values and the words

Target Market(s)

Myself & my team

Industry/Entity Type

Real Estate

Font styles to use
Other font styles liked:
• Company fonts as seen on our website

```html
<!DOCTYPE html>
<html lang="en">
<head>
<meta charset="UTF-8">
<title>Talvendo — Mission &amp; Values Poster</title>
<link href="https://fonts.googleapis.com/css2?family=Poppins:wght@300;400;800&display=swap" rel="stylesheet">
<style>
  :root {
    --page-bg: #e9ebea;
    --poster-green: #0b3a31;
    --word-dark: #4b6058;
    --word-light: #8a9690;
    --text-light: #f2f4f3;
    --icon-disc: #c4c8c6;
    --icon-ink: #1f2a27;
    --rule: #9aa8a2;
  }
  * { margin: 0; padding: 0; box-sizing: border-box; }
  html, body {
    width: 1200px; height: 1000px; overflow: hidden;
    background: var(--page-bg);
    font-family: "Poppins", sans-serif;
  }
  .poster {
    position: absolute; left: 267px; top: 30px;
    width: 665px; height: 940px;
    background: var(--poster-green);
    color: var(--text-light);
    box-shadow: 0 6px 18px rgba(0,0,0,.25);
    overflow: hidden;
  }
  .brand {
    position: absolute; right: 41px; top: 34px;
    font-weight: 400; font-size: 31px; letter-spacing: .14em;
    line-height: 1; color: var(--text-light);
  }
  .display {
    position: absolute; font-weight: 800; font-size: 87px;
    line-height: 1; letter-spacing: -.01em; white-space: nowrap;
  }
  .display--dark { color: var(--word-dark); }
  .display--light { color: var(--word-light); }
  .mission-our { left: 194px; top: 95px; }
  .mission-word { left: 49px; top: 159px; }
  .values-our { left: 321px; top: 396px; }
  .values-word { left: 206px; top: 460px; }
  .mission-tagline {
    position: absolute; left: 51px; top: 238px;
    font-size: 21px; font-weight: 400;
  }
  .mission-body {
    position: absolute; left: 51px; top: 288px; width: 385px;
    font-size: 10.6px; font-weight: 300; line-height: 12.2px;
    text-align: justify;
  }
  .values-intro {
    position: absolute; left: 218px; top: 540px; width: 410px;
    font-size: 21px; line-height: 25px; font-weight: 400;
  }
  .value { position: absolute; width: 310px; }
  .value__icon {
    position: absolute; left: 0; top: 22px;
    width: 52px; height: 52px; border-radius: 50%;
    background: var(--icon-disc);
  }
  .value__icon svg { width: 52px; height: 52px; display: block; }
  .value__title {
    position: absolute; left: 63px; top: 0;
    font-size: 19px; font-weight: 400; line-height: 22px;
  }
  .value__text {
    position: absolute; left: 63px; top: 20px; width: 228px;
    font-size: 10.1px; font-weight: 300; line-height: 12.2px;
    text-align: justify;
  }
  .value--love { left: 33px; top: 660px; }
  .value--team { left: 336px; top: 660px; }
  .value--thinking { left: 33px; top: 793px; }
  .value--zoe { left: 336px; top: 793px; }
  .value--thinking .value__icon, .value--zoe .value__icon { top: 18px; }
  .footer-rule {
    position: absolute; left: 36px; top: 904px;
    width: 592px; height: 1px; background: var(--rule);
  }
</style>
</head>
<body>
  <main class="poster">
    <div class="brand">TALVENDO</div>

    <h1 class="display display--dark mission-our">OUR</h1>
    <h1 class="display display--light mission-word">MISSION</h1>
    <p class="mission-tagline">Creating homes for abundant life.</p>
    <p class="mission-body">We wholeheartedly believe that home is an extraordinary place: a haven where life unfolds in all its glory. Where we find solace, make cherished memories with loved ones, and savour the natural beauty that surrounds us.</p>

    <h2 class="display display--dark values-our">OUR</h2>
    <h2 class="display display--light values-word">VALUES</h2>
    <p class="values-intro">We believe business can be a force for good. Our values shape the way we work, and how we make decisions.</p>

    <section class="value value--love">
      <div class="value__icon">
        <svg viewBox="0 0 52 52" fill="none" stroke="var(--icon-ink)" stroke-width="1.4" stroke-linejoin="round">
          <path d="M30 37 C22 31 17 26 17 21 a5 5 0 0 1 9-3 a5 5 0 0 1 9 3 c0 5-5 10-5 16z"/>
          <path d="M22 39 C15 35 11 31 11 27 a4.5 4.5 0 0 1 8-2.5 a4.5 4.5 0 0 1 8 2.5 c0 4-5 8-5 12z"/>
        </svg>
      </div>
      <h3 class="value__title">Love</h3>
      <p class="value__text">Our mission is founded in our love and respect for people - those we develop for, those in our teams and those in the communities we create and operate within.</p>
    </section>

    <section class="value value--team">
      <div class="value__icon">
        <svg viewBox="0 0 52 52" fill="none" stroke="var(--icon-ink)" stroke-width="1.4">
          <circle cx="20" cy="19" r="5"/><circle cx="32" cy="19" r="5"/>
          <circle cx="20" cy="33" r="5"/><circle cx="32" cy="33" r="5"/>
          <circle cx="26" cy="26" r="3" fill="var(--icon-ink)"/>
        </svg>
      </div>
      <h3 class="value__title">Team</h3>
      <p class="value__text">Property development is a team sport. We surround ourselves with the best designers and advisers. We strive to create an environment that allows them to do their best work and love doing it.</p>
    </section>

    <section class="value value--thinking">
      <div class="value__icon">
        <svg viewBox="0 0 52 52" fill="none" stroke="var(--icon-ink)" stroke-width="1.4" stroke-linecap="round">
          <path d="M21 31 a9 9 0 1 1 10 0 v4 h-10z"/>
          <path d="M22 38 h8 M23 41 h6"/>
          <path d="M26 17 v12 M22 22 h8"/>
          <path d="M14 22 h-3 M41 22 h-3 M17 14 l-2-2 M35 14 l2-2"/>
        </svg>
      </div>
      <h3 class="value__title">Thinking</h3>
      <p class="value__text">We believe in the power of thinking. Our rigorous and creative processes create beautifully considered solutions for our purchasers, the communities we develop within and the environment.</p>
    </section>

    <section class="value value--zoe">
      <div class="value__icon">
        <svg viewBox="0 0 52 52" fill="none" stroke="var(--icon-ink)" stroke-width="1.4" stroke-linejoin="round" stroke-linecap="round">
          <path d="M26 34 C19 29 15 25 15 20 a5 5 0 0 1 11-2 a5 5 0 0 1 11 2 c0 5-4 9-11 14z"/>
          <path d="M16 24 h5 l2-4 l3 7 l2-4 h8"/>
          <path d="M12 30 l6 7 h5 M40 30 l-6 7 h-5"/>
        </svg>
      </div>
      <h3 class="value__title">Zoe</h3>
      <p class="value__text">Our mission is to create places for ‘Zoe’ - the Greek word for abundant life. We do this through exquisite design, quality construction and celebrating nature.</p>
    </section>

    <div class="footer-rule"></div>
  </main>
</body>
</html>
```